Summit Builders Web Site / Business Cards

Construction Company that specializes in Water and Fire Damage, Residential ReModels, Landscaping and Building ADU (Accessory Dwelling Unit)

Growing and changing families often need additional space, and a remodeling project can often provide that. Adding a new area, or repurposing an existing one can satisfy this requirement.

Other times, homeowners want to update the look in their kitchen or bathroom with more than just a change of cabinetry or vanity doors and drawers. Whatever your needs are, Summit Builders has skilled workers who are bonded and insured, and ready to make your dreams and visions a reality.

Target Market(s)

Home Owners

Industry/Entity Type

Construction Company

Contact Information for Business Card

Center Logo with our information on the corners

Back side to be Logo Only
Contact Info
CSLB License # 4829516
info@summitbuildersca.example
www.summitbuildersca.example

Coding

Coded - Design and coding required

Number of Pages Required

5+ page

Font styles to use
Serif
Sans Serif

Requirements
Must have
• Using our Logo Colors
Home
About Us
Services
Projects / Portfolio
Contact Us
Nice to have
• Colors matching our Logo
Should not have
• Black because it doesnt match our logo

```html
<!DOCTYPE html>
<html lang="en">
<head>
<meta charset="utf-8">
<title>Summit Builders</title>
<link href="https://fonts.googleapis.com/css2?family=Poppins:wght@300;400;500;600&family=Oswald:wght@500;600&display=swap" rel="stylesheet">
<style>
:root{
  --orange:#ff6a00;
  --orange-dark:#e85d00;
  --ink:#2a2420;
  --text:#555;
  --muted:#8a8a8a;
  --light:#f3f3f3;
  --line:#e4e4e4;
  --white:#fff;
  --charcoal:#302a26;
}
*{margin:0;padding:0;box-sizing:border-box}
html,body{width:1200px;height:4501px;overflow:hidden}
body{position:relative;font-family:"Poppins",sans-serif;color:var(--text);background:var(--white)}
.abs{position:absolute}
.accent{color:var(--orange)}
.btn{position:absolute;display:flex;align-items:center;justify-content:center;gap:10px;background:var(--orange);color:#fff;font-size:13px;border-radius:6px}
.section-title{position:absolute;left:0;width:1200px;text-align:center;font-size:33px;font-weight:400;color:var(--ink);letter-spacing:.5px}

/* top bar */
.topbar-iso{left:670px;top:0;width:130px;height:30px;background:var(--charcoal);color:#fff;font-size:13px;display:flex;align-items:center;justify-content:center}
.topbar-contact{left:800px;top:0;width:400px;height:30px;background:var(--orange);color:#fff;font-size:13px;display:flex;align-items:center;padding-left:14px;gap:10px}
.topbar-contact .social{display:flex;gap:14px;margin-left:22px}
.topbar-contact .social span{width:11px;height:11px;border-radius:50%;background:#fff;opacity:.9}
.header{left:0;top:30px;width:1200px;height:70px;background:#fff;border-bottom:1px solid var(--line)}
.brand{left:160px;top:52px;display:flex;align-items:center;gap:10px;font-size:20px;font-weight:600;color:var(--ink)}
.brand i{width:18px;height:18px;background:var(--orange);display:block}
.nav{left:543px;top:57px;display:flex;gap:26px;font-size:12px;color:#666}
.nav .active{color:var(--orange);border-bottom:1px solid var(--orange)}

/* hero */
.hero{left:0;top:100px;width:1200px;height:575px;background:
  linear-gradient(180deg,rgba(30,30,40,.15) 0%,rgba(20,18,16,.35) 100%),
  linear-gradient(100deg,#5d6776 0%,#6e7480 30%,#7a5444 58%,#8a5a42 72%,#4c4a46 100%)}
.hero-curve{left:0;top:560px;width:1200px;height:120px}
.hero-title{left:0;top:270px;width:1200px;text-align:center;font-family:"Oswald",sans-serif;font-weight:600;font-size:78px;color:#fff;line-height:1}
.hero-sub{left:0;top:372px;width:1200px;text-align:center;font-family:"Oswald",sans-serif;font-weight:600;font-size:34px;color:var(--orange);letter-spacing:1px}
.hero-btn{left:525px;top:437px;width:149px;height:34px}
.hero-arrow{width:42px;height:42px}
.hero-badge{left:560px;top:600px;width:80px;height:80px;border-radius:50%;background:#fff}
.hero-badge i{position:absolute;left:28px;top:24px;width:24px;height:24px;background:var(--orange)}

/* what we do */
.wwd-band{left:0;top:675px;width:1200px;height:688px;background:linear-gradient(180deg,#fff 0%,#fff 30%,#f1f1f1 100%)}
.wwd-lead{left:0;top:780px;width:1200px;text-align:center;font-size:12.5px;line-height:21px;color:#666}
.card{position:absolute;top:877px;width:240px;height:314px;background:#fff;box-shadow:0 2px 10px rgba(0,0,0,.06);padding:0 22px}
.card svg{position:absolute;left:26px;top:35px}
.card h3{position:absolute;left:24px;top:156px;font-size:14.5px;font-weight:500;color:var(--ink);line-height:21px}
.card hr{position:absolute;left:120px;right:22px;top:133px;border:0;border-top:1px solid var(--line)}
.card p{position:absolute;left:22px;right:18px;top:210px;font-size:10.5px;line-height:19px;color:#777}
.card .more{position:absolute;left:24px;top:276px;font-size:10.5px;color:var(--ink);display:flex;align-items:center;gap:8px}
.card .more b{width:15px;height:15px;border-radius:50%;background:var(--orange);display:block}
.card.featured{top:868px;height:360px;background:linear-gradient(160deg,#ff7a1a 0%,#f06a10 55%,#d2702e 80%,#b9683a 100%)}
.card.featured h3,.card.featured p,.card.featured .more{color:#fff}
.card.featured h3{top:178px}.card.featured p{top:234px}.card.featured .more{top:315px}
.card.featured .more b{background:#fff}
.card.featured hr{border-color:rgba(255,255,255,.4);top:155px}
.wwd-link{left:0;top:1272px;width:1200px;text-align:center;font-size:12px;color:#555;text-decoration:underline}
.wwd-link b{color:var(--orange);font-weight:600}

/* who we are */
.who{left:0;top:1424px;width:600px;height:516px;background:var(--orange);color:#fff}
.who-photo{left:600px;top:1361px;width:600px;height:505px;background:
  linear-gradient(180deg,rgba(255,240,215,.25) 0%,rgba(0,0,0,0) 40%,rgba(60,40,25,.35) 100%),
  linear-gradient(110deg,#c9a57a 0%,#e2c59b 35%,#b88d5f 60%,#8a6a4f 85%,#6a5647 100%)}
.who-badge{left:668px;top:1822px;width:92px;height:92px;background:var(--orange);display:flex;align-items:flex-end;justify-content:center;padding-bottom:12px;color:#fff;font-size:10px;font-weight:600;white-space:nowrap}
.who h2{position:absolute;left:162px;top:50px;font-size:32px;font-weight:400;color:var(--ink)}
.who h4{position:absolute;left:162px;top:120px;font-size:18px;font-weight:400}
.who p{position:absolute;left:162px;top:158px;width:345px;font-size:11px;line-height:21px}
.feat{position:absolute;display:flex;align-items:center;gap:12px;font-size:12.5px;line-height:19px}
.feat span{width:50px;height:50px;border-radius:50%;background:#fff;display:flex;align-items:center;justify-content:center;flex:none}

/* projects */
.proj-sub{left:0;top:2066px;width:1200px;text-align:center;font-size:12px;color:#444}
.tabs{left:0;top:2114px;width:1200px;display:flex;justify-content:center;gap:26px;font-size:12px;color:#666}
.tabs .active{color:var(--orange);text-decoration:underline}
.proj-img{position:absolute;top:2172px;height:305px}
.proj-cap{position:absolute;top:2427px;width:296px;height:101px;background:#fff;box-shadow:0 4px 12px rgba(0,0,0,.08);padding:30px 0 0 70px}
.proj-cap:before{content:"";position:absolute;left:30px;top:41px;width:22px;height:2px;background:var(--orange)}
.proj-cap h5{font-size:18px;font-weight:400;color:var(--ink)}
.proj-cap p{font-size:10.5px;margin-top:6px;color:#777}
.proj-cap.active{background:var(--orange)}
.proj-cap.active h5,.proj-cap.active p{color:#fff}
.proj-cap.active:before{background:#fff}
.dots{left:0;width:1200px;display:flex;justify-content:center;gap:10px}
.dots i{width:8px;height:8px;border-radius:50%;border:1px solid #999;display:block}
.dots i.on{background:var(--orange);border-color:var(--orange)}

/* cta */
.cta-img{left:175px;top:2629px;width:425px;height:341px;background:linear-gradient(90deg,#ececec 0%,#f2f0ee 35%,#e9d8c6 55%,#9a7a5e 70%,#c9b9a6 85%,#f5f2ee 100%)}
.cta-line{left:0;top:2968px;width:600px;height:2px;background:#e8e8e8}
.cta h2{position:absolute;left:641px;top:2708px;font-size:32px;font-weight:400;color:var(--ink)}
.cta p{position:absolute;left:643px;top:2770px;width:310px;font-size:12px;line-height:21px;color:#666}
.cta-btn{left:645px;top:2855px;width:150px;height:34px}

/* stats */
.stats{left:0;top:2970px;width:1200px;height:490px;background:
  linear-gradient(90deg,rgba(0,0,0,0) 60%,rgba(40,60,70,.5) 100%),
  linear-gradient(180deg,#4a3b30 0%,#5e4b3d 40%,#4d4843 70%,#3b4448 100%)}
.stat{position:absolute;top:3068px;width:200px;text-align:center;color:#fff}
.stat b{display:block;font-size:33px;font-weight:400}
.stat span{display:block;font-size:14px;line-height:20px;margin-top:8px}

/* estimate */
.est-left{left:245px;top:3255px;width:298px;height:390px;background:var(--orange);color:#fff;text-align:center}
.est-left h2{position:absolute;left:0;width:298px;top:158px;font-size:33px;font-weight:400;line-height:41px}
.est-left p{position:absolute;left:0;width:298px;top:253px;font-size:12.5px;line-height:20px}
.est-right{left:543px;top:3255px;width:413px;height:390px;background:#f0f0f0}
.field{position:absolute;background:#fff;border:1px solid #e2e2e2;font-size:10px;color:#999;padding:10px 12px}
.submit{left:694px;top:3536px;width:110px;height:35px}

/* testimonial */
.avatar{left:300px;top:3794px;width:144px;height:144px;border-radius:50%;background:radial-gradient(circle at 50% 45%,#e8dfd8 0%,#cdbfb5 60%,#b5a79d 100%)}
.quote{left:487px;top:3808px;width:420px;font-size:13px;line-height:24px;color:#444}
.cite{left:497px;top:3943px;font-size:15px;color:var(--orange);padding-left:22px}
.cite:before{content:"";position:absolute;left:0;top:11px;width:13px;height:2px;background:var(--orange)}
.cite small{display:block;font-size:10.5px;color:#777;margin:2px 0 0 0}

/* footer */
.footer{left:0;top:4160px;width:1200px;height:292px}
.fcol{position:absolute;top:4210px;font-size:11px;color:#ddd;line-height:22px}
.fcol h6{font-size:13px;font-weight:500;color:#fff;margin-bottom:14px}
.fcol h6 em{font-style:normal;color:var(--orange)}
.fcol li{list-style:none;padding-left:18px;position:relative}
.fcol li:before{content:"";position:absolute;left:0;top:9px;width:5px;height:5px;border-radius:50%;background:var(--orange)}
.fcol li.on{color:var(--orange)}
.frow{display:flex;gap:12px;align-items:flex-start;margin-bottom:8px;line-height:18px}
.frow svg{flex:none;margin-top:2px}
.fbrand{left:862px;top:4290px;width:160px;text-align:center;font-size:22px;font-weight:600;color:#fff}
.fsocial{left:865px;top:4355px;display:flex;gap:10px}
.fsocial i{width:31px;height:31px;border-radius:50%;background:var(--orange);display:block}
.copy{left:0;top:4451px;width:1200px;height:50px;background:var(--orange);color:#fff;font-size:11px;display:flex;align-items:center;justify-content:center}
</style>
</head>
<body>

<!-- top bar & header -->
<div class="abs topbar-iso">ISO 9001:2017</div>
<div class="abs topbar-contact">
  <svg width="16" height="16" viewBox="0 0 24 24" fill="#fff"><path d="M6.6 10.8a15 15 0 0 0 6.6 6.6l2.2-2.2c.3-.3.7-.4 1-.2 1.1.4 2.3.6 3.6.6.6 0 1 .4 1 1V20c0 .6-.4 1-1 1A17 17 0 0 1 3 4c0-.6.4-1 1-1h3.5c.6 0 1 .4 1 1 0 1.3.2 2.5.6 3.6.1.3 0 .7-.2 1z"/></svg>
  1 555 310 2284
  <div class="social"><span></span><span></span><span></span></div>
</div>
<div class="abs header"></div>
<div class="abs brand"><i></i>Summit Builders</div>
<nav class="abs nav"><span class="active">Home</span><span>About Us</span><span>Projects</span><span>Services</span><span>Contact</span></nav>
<div class="btn" style="left:889px;top:48px;width:151px;height:35px">GET A QUOTE
  <svg width="14" height="14" viewBox="0 0 24 24" fill="none" stroke="#fff" stroke-width="2"><path d="M4 20l4-1 11-11-3-3L5 16z"/></svg></div>

<!-- hero -->
<div class="abs hero" role="img" aria-label="Large two-storey brick home with dark roof at dusk"></div>
<svg class="abs hero-curve" viewBox="0 0 1200 120" preserveAspectRatio="none"><path d="M0 115 C300 30 450 55 600 60 C750 55 900 30 1200 115 L1200 120 L0 120Z" fill="#fff"/></svg>
<div class="abs hero-title">The Best Choose us</div>
<div class="abs hero-sub">Because We Deliver</div>
<div class="btn hero-btn">GET A QUOTE
  <svg width="14" height="14" viewBox="0 0 24 24" fill="none" stroke="#fff" stroke-width="2"><path d="M4 20l4-1 11-11-3-3L5 16z"/></svg></div>
<svg class="abs hero-arrow" style="left:62px;top:336px" viewBox="0 0 42 42"><rect x="9" y="9" width="24" height="24" transform="rotate(45 21 21)" fill="none" stroke="#fff" stroke-width="1.5"/><path d="M24 15l-6 6 6 6" fill="none" stroke="#fff" stroke-width="1.5"/></svg>
<svg class="abs hero-arrow" style="left:1097px;top:336px" viewBox="0 0 42 42"><rect x="9" y="9" width="24" height="24" transform="rotate(45 21 21)" fill="#ff6a00"/><path d="M18 15l6 6-6 6" fill="none" stroke="#fff" stroke-width="1.5"/></svg>
<div class="abs hero-badge"><i></i></div>

<!-- what we do -->
<div class="abs wwd-band"></div>
<h2 class="section-title" style="top:730px">WHAT <span class="accent">WE DO</span></h2>
<p class="abs wwd-lead">Construction Company that specializes in Water and Fire Damage,<br>Residential ReModels, Landscaping and Building ADU.</p>

<div class="card" style="left:210px">
  <svg width="72" height="72" viewBox="0 0 72 72" fill="none" stroke="#2a2420" stroke-width="2"><path d="M6 36 L36 10 L66 36"/><path d="M14 30v34h44V30"/><rect x="22" y="44" width="10" height="20"/><rect x="40" y="42" width="12" height="12"/><path d="M46 42v12M40 48h12"/><path d="M48 18v-6h6v11" stroke="#ff6a00"/></svg>
  <hr><h3>Home<br>Construction</h3>
  <p>Lorem ipsum is simply dummy text of the printing and typesetting this Lorem ipsum has.</p>
  <div class="more">Read More <b></b></div>
</div>
<div class="card featured" style="left:480px" role="img" aria-label="Orange tinted photo of a worker remodeling a room">
  <svg width="72" height="72" viewBox="0 0 72 72" fill="none" stroke="#fff" stroke-width="2"><rect x="26" y="16" width="20" height="50"/><rect x="12" y="36" width="14" height="30"/><rect x="46" y="30" width="14" height="36"/><path d="M36 6v10M31 24h10M31 32h10M31 40h10M31 48h10M16 44h6M16 52h6M50 38h6M50 46h6"/></svg>
  <hr><h3>Building<br>Remodeling</h3>
  <p>Lorem ipsum is simply dummy text of the printing and typesetting this Lorem ipsum has.</p>
  <div class="more">Read More <b></b></div>
</div>
<div class="card" style="left:749px">
  <svg width="72" height="72" viewBox="0 0 72 72" fill="none" stroke="#2a2420" stroke-width="2"><path d="M8 30 L32 10 L56 30"/><rect x="14" y="26" width="36" height="36"/><rect x="20" y="34" width="8" height="8"/><rect x="32" y="34" width="8" height="8"/><rect x="20" y="46" width="8" height="8"/><path d="M46 40l12-4 12 4v10c0 8-6 12-12 15-6-3-12-7-12-15z" fill="#ff6a00" stroke="#ff6a00"/><path d="M58 40v22M48 50h20" stroke="#fff"/></svg>
  <hr><h3>Safety<br>Management</h3>
  <p>Lorem ipsum is simply dummy text of the printing and typesetting this Lorem ipsum has.</p>
  <div class="more">Read More <b></b></div>
</div>
<svg class="abs" style="left:58px;top:1010px" width="44" height="44" viewBox="0 0 44 44"><rect x="10" y="10" width="24" height="24" transform="rotate(45 22 22)" fill="#fff" stroke="#333" stroke-width="1.2"/><path d="M25 16l-6 6 6 6" fill="none" stroke="#333" stroke-width="1.5"/></svg>
<svg class="abs" style="left:1098px;top:1010px" width="44" height="44" viewBox="0 0 44 44"><rect x="10" y="10" width="24" height="24" transform="rotate(45 22 22)" fill="#ff6a00"/><path d="M19 16l6 6-6 6" fill="none" stroke="#fff" stroke-width="1.5"/></svg>
<p class="abs wwd-link">Offering high quality construction solutions. <b>Build Your Dream Now!</b></p>

<!-- who we are -->
<div class="abs who-photo" role="img" aria-label="Two workers installing new light wood kitchen cabinets"></div>
<section class="abs who">
  <h2>WHO WE ARE</h2>
  <h4>We Deliver Landmark Projects</h4>
  <p>We are rethoric question ran over her cheek When she reached the first hills of the Italic Mountains, she had a last view back on the skyline of her hometown Bookmarksgrove, the headline of Alphabet Village and the subline of her own road, the Line Lane.</p>
  <div class="feat" style="left:160px;top:300px"><span><svg width="28" height="28" viewBox="0 0 24 24" fill="none" stroke="#ff6a00" stroke-width="1.5"><path d="M12 3l2.7 5.6 6.1.9-4.4 4.3 1 6.1L12 17l-5.4 2.9 1-6.1L3.2 9.5l6.1-.9z"/></svg></span>We've Reputionl<br>For Excellence</div>
  <div class="feat" style="left:358px;top:300px"><span><svg width="30" height="30" viewBox="0 0 24 24" fill="none" stroke="#ff6a00" stroke-width="1.4"><path d="M2 10l4-3 4 2 3-2 4 1 5 3M6 13l3 3c1 1 2 1 3 0l4-4M9 14l2 2M12 12l2 2"/></svg></span>We Build<br>Partnerships</div>
  <div class="feat" style="left:160px;top:392px"><span><svg width="28" height="28" viewBox="0 0 24 24" fill="none" stroke="#ff6a00" stroke-width="1.5"><path d="M3 11h4v9H3zM7 11l4-7c1.5 0 2 1 2 2v4h6c1 0 2 1 1.8 2l-1.5 6c-.2 1-1 2-2 2H7"/></svg></span>Guided By<br>Commitment</div>
  <div class="feat" style="left:358px;top:392px"><span><svg width="30" height="30" viewBox="0 0 24 24" fill="none" stroke="#ff6a00" stroke-width="1.4"><circle cx="12" cy="8" r="3"/><circle cx="5" cy="11" r="2.2"/><circle cx="19" cy="11" r="2.2"/><path d="M6 20c0-4 3-6 6-6s6 2 6 6M1 20c0-3 2-5 4-5M23 20c0-3-2-5-4-5"/></svg></span>A Team of<br>Professionals</div>
</section>
<div class="abs who-badge">Summit Builders</div>

<!-- recent projects -->
<h2 class="section-title" style="top:2020px">RECENT <span class="accent">PROJECTS</span></h2>
<p class="abs proj-sub">Summit Builders Work</p>
<nav class="abs tabs"><span class="active">All</span><span>Remodeling</span><span>Exterior</span><span>Interior</span><span>Renovation</span><span>Construction</span></nav>
<div class="proj-img" style="left:0;width:360px;background:linear-gradient(90deg,#3f3b38 0%,#8e8479 25%,#d8cdbd 45%,#ebe6de 70%,#cfc6ba 100%)" role="img" aria-label="Remodeled open living room with wood shelving"></div>
<div class="proj-img" style="left:419px;width:360px;background:linear-gradient(180deg,#7d8288 0%,#a9adb1 30%,#4a4a4c 55%,#2f3032 72%,#8a8580 100%)" role="img" aria-label="Modern two-storey house exterior with dark cladding"></div>
<div class="proj-img" style="left:840px;width:360px;background:linear-gradient(180deg,#f3efe9 0%,#e6ddd0 35%,#8b6a57 60%,#5f4638 85%,#a08570 100%)" role="img" aria-label="Renovated kitchen interior with brown cabinets"></div>
<div class="proj-cap active" style="left:30px"><h5>Remodeling</h5><p>Lorem ipsum is simply text.</p></div>
<div class="proj-cap" style="left:452px"><h5>Exterior</h5><p>Lorem ipsum is simply text.</p></div>
<div class="proj-cap" style="left:872px"><h5>Interior</h5><p>Lorem ipsum is simply text.</p></div>
<div class="abs dots" style="top:2573px"><i class="on"></i><i></i><i></i><i></i></div>

<!-- project cta -->
<div class="abs cta-img" role="img" aria-label="Smiling builder in yellow hard hat with arms crossed beside a faint building outline"></div>
<div class="abs cta-line"></div>
<section class="cta">
  <h2>Have Any <span class="accent">Project ?</span></h2>
  <p>Construction Company that specializes in Water and Fire Damage, Residential ReModels, Landscaping and Building ADU.</p>
</section>
<div class="btn cta-btn">GET A QUOTE
  <svg width="14" height="14" viewBox="0 0 24 24" fill="none" stroke="#fff" stroke-width="2"><path d="M4 20l4-1 11-11-3-3L5 16z"/></svg></div>

<!-- stats -->
<div class="abs stats" role="img" aria-label="Water damaged kitchen flooded with water"></div>
<div class="stat" style="left:157px"><b>53</b><span>Total<br>Projects</span></div>
<div class="stat" style="left:384px"><b>371</b><span>Staff<br>Members</span></div>
<div class="stat" style="left:611px"><b>15</b><span>Working In<br>States</span></div>
<div class="stat" style="left:835px"><b>2600</b><span>Hours For<br>Work</span></div>

<!-- estimate -->
<section class="abs est-left">
  <svg class="abs" style="left:118px;top:65px" width="62" height="62" viewBox="0 0 62 62" fill="none" stroke="#fff" stroke-width="1.5"><rect x="13" y="13" width="36" height="36" transform="rotate(45 31 31)"/><path d="M24 38l2-6 10-10 4 4-10 10z"/></svg>
  <h2>GET A FREE<br>ESTIMATE</h2>
  <p>If you have an any Question For<br>Contact Us Today !</p>
  <svg class="abs" style="left:128px;top:320px" width="42" height="14" viewBox="0 0 42 14" fill="none" stroke="#fff" stroke-width="2"><path d="M0 7h38M32 1l6 6-6 6"/></svg>
</section>
<section class="abs est-right"></section>
<div class="field" style="left:582px;top:3330px;width:164px;height:37px">Name *</div>
<div class="field" style="left:762px;top:3330px;width:164px;height:37px">Email *</div>
<div class="field" style="left:582px;top:3386px;width:164px;height:37px">Phone *</div>
<div class="field" style="left:762px;top:3386px;width:164px;height:37px">Services<svg style="position:absolute;right:10px;top:15px" width="8" height="6" viewBox="0 0 8 6"><path d="M0 0h8L4 6z" fill="#ff6a00"/></svg></div>
<div class="field" style="left:582px;top:3438px;width:344px;height:80px">Your Question *</div>
<div class="btn submit">SUBMIT</div>

<!-- testimonial -->
<h2 class="section-title" style="top:3715px">WHAT OUR <span class="accent">CLIENT SAY</span></h2>
<div class="abs avatar" role="img" aria-label="Portrait of a smiling client"></div>
<p class="abs quote">"Summit Builders is one of the best General contractors we've worked with. The entire team tactfully delivered a project of Exceptional Quality while staying on Schedule and under budget. We hope to work with Summit again in the Near Future!"</p>
<div class="abs cite">Clara Weston<small>Project Manager</small></div>
<div class="abs dots" style="top:4038px"><i class="on"></i><i></i><i></i><i></i></div>

<!-- footer -->
<svg class="abs footer" viewBox="0 0 1200 292" preserveAspectRatio="none"><path d="M0 40 Q600 -10 1200 40 L1200 292 L0 292Z" fill="#302a26"/><path d="M0 40 Q600 -10 1200 40" fill="none" stroke="#ff6a00" stroke-width="3"/></svg>
<div class="fcol" style="left:162px">
  <h6>SITE<em>MAP</em></h6>
  <ul><li class="on">Home</li><li>About Us</li><li>Services</li><li>Projects</li><li>Contact</li></ul>
</div>
<div class="fcol" style="left:363px;width:230px">
  <h6>CONTACT <em>US</em></h6>
  <div class="frow"><svg width="14" height="14" viewBox="0 0 24 24" fill="#ff6a00"><path d="M12 2a7 7 0 0 0-7 7c0 5 7 13 7 13s7-8 7-13a7 7 0 0 0-7-7zm0 9.5A2.5 2.5 0 1 1 12 6a2.5 2.5 0 0 1 0 5.5z"/></svg><span>412 W Cedar Ridge Ave<br>Fairview, CA 90000</span></div>
  <div class="frow"><svg width="14" height="14" viewBox="0 0 24 24" fill="#ff6a00"><path d="M6.6 10.8a15 15 0 0 0 6.6 6.6l2.2-2.2c.3-.3.7-.4 1-.2 1.1.4 2.3.6 3.6.6.6 0 1 .4 1 1V20c0 .6-.4 1-1 1A17 17 0 0 1 3 4c0-.6.4-1 1-1h3.5c.6 0 1 .4 1 1 0 1.3.2 2.5.6 3.6.1.3 0 .7-.2 1z"/></svg><span>555-310-4471</span></div>
  <div class="frow"><svg width="14" height="14" viewBox="0 0 24 24" fill="#ff6a00"><rect x="3" y="5" width="18" height="14" rx="2"/></svg><span>555-310-8826</span></div>
  <div class="frow"><svg width="14" height="14" viewBox="0 0 24 24" fill="none" stroke="#ff6a00" stroke-width="2"><rect x="3" y="5" width="18" height="14"/><path d="M3 6l9 7 9-7"/></svg><span>hello@summitbuildersca.example</span></div>
  <div class="frow"><svg width="14" height="14" viewBox="0 0 24 24" fill="#ff6a00"><path d="M6.6 10.8a15 15 0 0 0 6.6 6.6l2.2-2.2c.3-.3.7-.4 1-.2 1.1.4 2.3.6 3.6.6.6 0 1 .4 1 1V20c0 .6-.4 1-1 1A17 17 0 0 1 3 4c0-.6.4-1 1-1h3.5c.6 0 1 .4 1 1 0 1.3.2 2.5.6 3.6.1.3 0 .7-.2 1z"/></svg><span>555-310-2284 (<em class="accent" style="font-style:normal">office</em>)</span></div>
</div>
<div class="fcol" style="left:612px;width:205px">
  <h6>WORKING <em>HOURS</em></h6>
  <p style="line-height:18px;margin-bottom:10px">We work 7 days a week, every day excluding major holidays. Contact us if you have an emergency, with our Hotline and Contact form.</p>
  <div class="frow"><svg width="14" height="14" viewBox="0 0 24 24" fill="none" stroke="#ff6a00" stroke-width="2"><circle cx="12" cy="12" r="9"/><path d="M12 7v5l3 2"/></svg><span>Mon-Fri: 10:00 – 16:00<br>Sat: 12:00 – 15:00<br>Sunday &amp; holidays: 09:00 – 12:00</span></div>
</div>
<div class="abs fbrand">Summit Builders</div>
<div class="abs fsocial"><i></i><i></i><i></i><i></i></div>
<div class="abs copy">©Summit Builders -2020 All rights reserved.</div>

</body>
</html>
```